Fin-Tech Firm Captivating Business Card Design

We need a logo design as well to compliment this business card.

We are a new startup based in Singapore called 'Quorvane Systems'.

We develop an array of financial solutions ranging from payment convenience to forex trading and remittance.

Our initial product is Pam - an application which allows user to pre-order food items which would be ready for pickup upon arrival.

We would like to see designs being in black and silver or whatever that looks appealing and exudes a fun and professional feel.

We're not picky as long as it doesn't look like common business cards will do.

I do have a current logo which i do not really like. It will be attached for reference sake

Info:

Quorvane Systems Pte. Ltd.
Company Registration no. 208817264K

FILE TO BE IN .AI and .PSD

Target Market(s)

-F&B (Online-Ordering)
-Finance(P2P Lending and Forex)

Industry/Entity Type

Finance

Contact Information for Business Card

Name
Position
Contact
Email
Address: 47 Bexley Lane, Harbourvale Tower, #14-03 Singapore 068215

Marcus Teo
Founder, Managing Director
+65 98471630
marcus.t@quorvanesys.com

Wei Lok
Founder, Executive Director
+65 96058243
wei.l@quorvanesys.com

Logo Text

Quorvane Systems

Font styles to use
Sans Serif

Requirements
Must have
• Something that has word play about link lynk
• Minimalistic but also something that catches The Eye
• Gold/silver on white/black might be nice
• Animal logo ; horse, eagle, bull or bear
Nice to have
• Just make it look fun and cute
• Just a suggestion to make the Y of quorvane stand out
Should not have
• Any landmarks of singapore
• Exclude Pte. Ltd.

```html
<!DOCTYPE html>
<html lang="en">
<head>
<meta charset="UTF-8">
<title>Quorvane Systems – Business Card</title>
<link href="https://fonts.googleapis.com/css2?family=Open+Sans:wght@400;600;700&display=swap" rel="stylesheet">
<style>
  :root {
    --paper: #ececee;
    --card-top: #242424;
    --card-bottom: #0c0c0c;
    --gold: #d9a828;
    --gold-light: #f4d67a;
    --gold-dark: #a8741a;
    --title-grey: #cfcfcf;
    --detail-grey: #b5b5b5;
  }
  * { margin: 0; padding: 0; box-sizing: border-box; }
  html, body {
    width: 1200px;
    height: 800px;
    overflow: hidden;
    background: var(--paper);
    font-family: "Open Sans", Arial, sans-serif;
  }
  .canvas {
    width: 1200px;
    height: 800px;
    display: flex;
    align-items: center;
    justify-content: center;
    gap: 40px;
  }
  .card {
    position: relative;
    width: 540px;
    height: 309px;
    background: linear-gradient(160deg, var(--card-top), var(--card-bottom));
    border-radius: 3px;
    box-shadow: 0 10px 24px rgba(0,0,0,0.25);
    overflow: hidden;
  }
  .gold-edge {
    position: absolute;
    left: 0;
    bottom: 0;
    width: 100%;
    height: 40px;
  }

  /* Front */
  .brand-mark {
    position: absolute;
    left: 0;
    right: 0;
    top: 108px;
    text-align: center;
    color: var(--gold);
    font-weight: 700;
    line-height: 1;
  }
  .brand-mark .brand-name {
    display: block;
    font-size: 44px;
    letter-spacing: 1px;
  }
  .brand-mark .brand-sub {
    display: block;
    font-size: 16px;
    letter-spacing: 5px;
    margin-top: 8px;
  }

  /* Back */
  .person {
    position: absolute;
    right: 40px;
    top: 44px;
    text-align: right;
  }
  .person-name {
    color: var(--gold);
    font-weight: 700;
    font-size: 26px;
    letter-spacing: 0.5px;
  }
  .person-title {
    color: var(--title-grey);
    font-size: 13px;
    letter-spacing: 0.6px;
    margin-top: 2px;
  }
  .contact-list {
    position: absolute;
    left: 30px;
    top: 56px;
    list-style: none;
  }
  .contact-list li {
    display: flex;
    align-items: flex-start;
    gap: 12px;
    color: var(--detail-grey);
    font-size: 11px;
    line-height: 1.45;
    margin-bottom: 8px;
  }
  .contact-list svg {
    flex: none;
    width: 13px;
    height: 13px;
    margin-top: 1px;
  }
  .brand-mark-small {
    position: absolute;
    right: 30px;
    bottom: 34px;
    text-align: center;
    color: var(--gold);
    font-weight: 700;
    line-height: 1;
  }
  .brand-mark-small .brand-name { display: block; font-size: 18px; }
  .brand-mark-small .brand-sub { display: block; font-size: 7px; letter-spacing: 2px; margin-top: 3px; }
</style>
</head>
<body>
<main class="canvas">

  <!-- Front of card -->
  <section class="card card-front" aria-label="Card front">
    <div class="brand-mark">
      <span class="brand-name">QUORVANE</span>
      <span class="brand-sub">SYSTEMS</span>
    </div>
    <svg class="gold-edge" viewBox="0 0 540 40" preserveAspectRatio="none" aria-hidden="true">
      <defs>
        <linearGradient id="goldFront" x1="0" x2="1" y1="0" y2="0">
          <stop offset="0" stop-color="var(--gold-dark)"/>
          <stop offset="0.3" stop-color="var(--gold-light)"/>
          <stop offset="0.7" stop-color="var(--gold)"/>
          <stop offset="1" stop-color="var(--gold-dark)"/>
        </linearGradient>
      </defs>
      <polygon points="0,20 540,34 540,40 0,40" fill="url(#goldFront)"/>
    </svg>
  </section>

  <!-- Back of card -->
  <section class="card card-back" aria-label="Card back">
    <div class="person">
      <div class="person-name">MARCUS TEO</div>
      <div class="person-title">FOUNDER, MANAGING DIRECTOR</div>
    </div>

    <ul class="contact-list">
      <li>
        <svg viewBox="0 0 24 24" aria-hidden="true"><path fill="var(--gold)" d="M6.6 10.8a15 15 0 0 0 6.6 6.6l2.2-2.2a1 1 0 0 1 1-.25 11.4 11.4 0 0 0 3.6.57 1 1 0 0 1 1 1V20a1 1 0 0 1-1 1A17 17 0 0 1 3 4a1 1 0 0 1 1-1h3.5a1 1 0 0 1 1 1c0 1.25.2 2.45.57 3.57a1 1 0 0 1-.25 1z"/></svg>
        <span>+65 98471630</span>
      </li>
      <li>
        <svg viewBox="0 0 24 24" aria-hidden="true"><circle cx="12" cy="12" r="11" fill="var(--gold)"/><path d="M6 8h12v8H6z" fill="none" stroke="#111" stroke-width="1.6"/><path d="M6 8l6 5 6-5" fill="none" stroke="#111" stroke-width="1.6"/></svg>
        <span>marcus.t@quorvanesys.com</span>
      </li>
      <li>
        <svg viewBox="0 0 24 24" aria-hidden="true"><path fill="var(--gold)" d="M12 2a7 7 0 0 0-7 7c0 5.2 7 13 7 13s7-7.8 7-13a7 7 0 0 0-7-7zm0 9.5A2.5 2.5 0 1 1 12 6.5a2.5 2.5 0 0 1 0 5z"/></svg>
        <span>47 Bexley Lane, Harbourvale Tower,<br>#14-03 Singapore 068215</span>
      </li>
    </ul>

    <div class="brand-mark-small">
      <span class="brand-name">QUORVANE</span>
      <span class="brand-sub">SYSTEMS</span>
    </div>

    <svg class="gold-edge" viewBox="0 0 540 40" preserveAspectRatio="none" aria-hidden="true">
      <defs>
        <linearGradient id="goldBack" x1="0" x2="1" y1="0" y2="0">
          <stop offset="0" stop-color="var(--gold-light)"/>
          <stop offset="0.35" stop-color="var(--gold)"/>
          <stop offset="0.6" stop-color="var(--gold-dark)"/>
          <stop offset="1" stop-color="var(--gold-dark)" stop-opacity="0"/>
        </linearGradient>
      </defs>
      <polygon points="0,16 320,40 0,40" fill="url(#goldBack)"/>
    </svg>
  </section>

</main>
</body>
</html>
```